Boutique growth strategy brochure

This may be a larger task than a traditional brochure. This is a brochure I had made up for my old company. I always liked it and it replicated my website ( although the website had more content). What I would like to do is make a similar brochure as far as style goes and I would also like to incorporate the same information into a new website. Some of the wording will need to be changed as well as the Company name and Logo. Is this something that you would be interested in working on ( Bothe the brochure and a website?)

Regards,
Brent

Target Market(s)

Mid sized business owners

Industry/Entity Type

Mid sized privately owned businesses largely service oriented

Colors

Designer to choose colors to be used in the design.

Requirements
Must have
• Professional look and feel
Nice to have
• This was a design from an old folder. I want to create something similar with the new company name (Harborline Venture Partners) or HVP logo

```html
<!DOCTYPE html>
<html lang="en">
<head>
<meta charset="utf-8">
<title>Harborline Venture Partners – Folder</title>
<link rel="stylesheet" href="https://fonts.googleapis.com/css2?family=Exo+2:ital,wght@0,400;0,800;1,600;1,800&display=swap">
<style>
  :root{
    --navy:#0c2a44;
    --navy-deep:#082036;
    --sky:#19a3e2;
    --blue:#1b5fa6;
    --paper:#ffffff;
    --mist:#eef0f3;
    --rule:#2b2b2b;
    --ink:#1c1c1c;
  }
  *{margin:0;padding:0;box-sizing:border-box}
  html,body{width:1200px;height:848px;overflow:hidden;background:var(--paper)}
  .folder{
    position:relative;width:1200px;height:848px;overflow:hidden;
    font-family:"Exo 2",sans-serif;color:var(--ink);
    background:var(--paper);
  }
  .backdrop{position:absolute;inset:0}
  .side-bar{position:absolute;top:90px;width:18px;height:667px;background:var(--navy)}
  .side-bar.left{left:0}
  .side-bar.right{right:0}

  .headline{position:absolute;top:62px;left:640px;width:490px;text-align:center}
  .headline .main{
    display:block;font-weight:800;font-style:italic;font-size:44px;
    color:var(--navy);letter-spacing:.5px;line-height:1.05;
  }
  .headline .sub{
    display:block;font-weight:800;font-style:italic;font-size:25px;
    color:var(--navy-deep);line-height:1.05;margin-top:2px;
  }
  .banner{position:absolute;top:148px;left:660px;width:456px;height:60px}
  .banner-text{
    position:absolute;top:0;left:0;width:456px;height:46px;
    display:flex;align-items:center;justify-content:center;
    font-weight:800;font-style:italic;font-size:35px;color:#fff;letter-spacing:.3px;
  }

  .photo{
    position:absolute;top:223px;left:18px;width:1164px;height:402px;
    background:linear-gradient(100deg,#173f78 0%,#1f66b0 35%,#1b8fd4 62%,#1aa5e3 100%);
  }
  .photo::before{
    content:"";position:absolute;inset:0;
    background:linear-gradient(135deg,rgba(255,255,255,.14) 0 30%,transparent 30%);
  }
  .fold{position:absolute;top:223px;left:600px;width:1px;height:402px;background:rgba(255,255,255,.45)}

  .tagline{
    position:absolute;top:708px;left:84px;
    font-weight:600;font-style:italic;font-size:33px;color:var(--navy);
  }
  .contact{position:absolute;left:58px;width:520px;font-size:14.5px;color:var(--ink)}
  .contact.address{top:771px;text-align:center}
  .contact.lines{top:798px;display:flex;gap:12px;justify-content:center}
  .contact span{display:inline-flex;align-items:center;gap:5px}
  .contact svg{width:14px;height:14px}

  .brand{
    position:absolute;top:690px;left:680px;display:flex;align-items:center;gap:16px;
  }
  .brand-square{width:22px;height:22px;background:var(--navy)}
  .brand-name{
    font-weight:800;color:var(--navy);line-height:.92;font-size:30px;letter-spacing:1px;
  }
  .brand-name .mark{font-size:58px;display:block;float:left;margin-right:18px;line-height:1.25}

  .base-rule{position:absolute;top:830px;left:50px;width:1106px;height:1px;background:var(--rule)}
</style>
</head>
<body>
<main class="folder">
  <svg class="backdrop" width="1200" height="848" viewBox="0 0 1200 848" aria-hidden="true">
    <polygon points="0,0 420,0 160,260 0,160" fill="#f4f5f7"/>
    <polygon points="320,0 600,0 600,220 520,220" fill="#f7f8f9"/>
    <polygon points="600,0 900,0 760,220 600,220" fill="#f3f4f6"/>
    <polygon points="960,0 1200,0 1200,200" fill="#f2f3f5"/>
    <polygon points="0,625 260,625 80,848 0,848" fill="#f1f2f4"/>
    <polygon points="320,625 600,625 600,848 160,848" fill="#f6f7f8"/>
    <polygon points="600,625 980,625 760,848 600,848" fill="#f2f3f5"/>
    <polygon points="1000,625 1200,625 1200,848 860,848" fill="#f6f7f8"/>
  </svg>

  <div class="side-bar left"></div>
  <div class="side-bar right"></div>

  <h1 class="headline">
    <span class="main">BUSSINESS GROWTH</span>
    <span class="sub">AND EXIT</span>
  </h1>
  <div class="banner">
    <svg width="456" height="60" viewBox="0 0 456 60" aria-hidden="true">
      <defs>
        <radialGradient id="bannerShadow" cx="50%" cy="0%" r="50%">
          <stop offset="0" stop-color="#000" stop-opacity=".35"/>
          <stop offset="1" stop-color="#000" stop-opacity="0"/>
        </radialGradient>
      </defs>
      <ellipse cx="228" cy="48" rx="200" ry="10" fill="url(#bannerShadow)"/>
      <polygon points="8,0 456,0 448,46 0,46" fill="var(--navy)"/>
    </svg>
    <div class="banner-text">STRATEGY SPECIALISTS</div>
  </div>

  <div class="photo" role="img" aria-label="Blue-toned photograph of a team of colleagues collaborating around laptops at an office table"></div>
  <div class="fold"></div>

  <p class="tagline">Harborline Venture Partners</p>
  <p class="contact address">
    <span>
      <svg viewBox="0 0 16 16" aria-hidden="true"><path d="M8 1.5a4 4 0 0 0-4 4c0 3 4 7 4 7s4-4 4-7a4 4 0 0 0-4-4z" fill="none" stroke="#1c1c1c" stroke-width="1.4"/><circle cx="8" cy="5.5" r="1.4" fill="#1c1c1c"/><path d="M2 14.5h12" stroke="#1c1c1c" stroke-width="1.2"/></svg>
      418 Quarry Lane N.E, Calgary, Alberta, Canada T2E 5K8
    </span>
  </p>
  <p class="contact lines">
    <span>
      <svg viewBox="0 0 16 16" aria-hidden="true"><circle cx="8" cy="8" r="6.5" fill="none" stroke="#1c1c1c" stroke-width="1.3"/><ellipse cx="8" cy="8" rx="2.8" ry="6.5" fill="none" stroke="#1c1c1c" stroke-width="1"/><path d="M1.5 8h13" stroke="#1c1c1c" stroke-width="1"/></svg>
      www.harborlinevp.com
    </span>
    <span>
      <svg viewBox="0 0 16 16" aria-hidden="true"><rect x="4" y="1.5" width="8" height="13" rx="1.5" fill="none" stroke="#1c1c1c" stroke-width="1.4"/><circle cx="8" cy="12" r=".9" fill="#1c1c1c"/></svg>
      Phone : 403.555.0148
    </span>
    <span>
      <svg viewBox="0 0 16 16" aria-hidden="true"><rect x="1.5" y="5" width="13" height="8.5" rx="1" fill="#1c1c1c"/><rect x="4" y="1.5" width="8" height="4" fill="none" stroke="#1c1c1c" stroke-width="1.2"/><rect x="9" y="7" width="4" height="1.3" fill="#fff"/></svg>
      Fax : 403.555.0192
    </span>
  </p>

  <div class="brand">
    <div class="brand-square"></div>
    <div class="brand-name"><span class="mark">HVP</span>HARBORLINE<br>VENTURE<br>PARTNERS</div>
  </div>

  <div class="base-rule"></div>
</main>
</body>
</html>
```